Healthy Food Healthy Brain Rack Card

We want a new 2 page (front and page) 3.67" x 8.5" rack card. This rack card is the first of a series we are creating. We will have five more eventually.

The minimum font size for the text on the front is 11 point and also for other main body text.

Use the text on the word document.

The images and layout in the word document are just sample ideas we had.

We have a subscripton to adobe stock images so prefer to get images from there or free high quality images.

The document is for older readers. Do not put text over graphics and keep it simple and easy to read with high contrast.

We are open to any color scheme, though something that conveys fresh and healthy, is good.

We want some very simple design element(s) incorporated that convey Native American communities or heritage. But NO head dress, teepee graphics, etc.

At the top, of the first page we would like a collage of healthy food images. This can include fish, chicken, fresh vegetables, berries, brown rice, etc.

On the back side, the text below the brown box on the word document with the title "mock up" can be smaller as needed.

Please remember to include the funding statement - it can be in a very small font 6/7 point.

For more information about our project, please visit https://velmorcollective.org/mind-care/

```html
<!DOCTYPE html>
<html lang="en">
<head>
<meta charset="utf-8">
<title>Healthy Food Healthy Brain – Rack Card</title>
<link rel="stylesheet" href="https://fonts.googleapis.com/css2?family=Chewy&family=Catamaran:wght@400;500;600;700&family=Arimo&display=swap">
<style>
  :root{
    --maroon:#5e0f10;
    --teal:#1a8791;
    --paper:#f4f2ef;
    --ink:#1c1c1c;
    --stage:#d6d6d6;
    --white:#ffffff;
  }
  *{margin:0;padding:0;box-sizing:border-box}
  html,body{width:1200px;height:1200px;overflow:hidden;background:var(--stage)}
  body{position:relative;font-family:"Catamaran","Trebuchet MS",sans-serif;color:var(--ink)}
  .card{position:absolute;top:150px;width:389px;height:900px;background:var(--paper);overflow:hidden;box-shadow:0 4px 18px rgba(0,0,0,.25)}
  .card--front{left:157px}
  .card--back{left:654px}
  .abs{position:absolute}
  .display{font-family:"Chewy","Comic Sans MS",cursive}

  /* front */
  .food-collage{left:0;top:0;width:389px;height:150px;background:linear-gradient(180deg,#8d6a4c 0%,#b9835f 45%,#e4d2c0 85%,var(--paper) 100%)}
  .title{left:0;width:389px;text-align:center;font-size:50px;line-height:1;white-space:nowrap}
  .title--food{top:152px;color:var(--maroon);text-shadow:2px 2px 0 var(--white),-2px -2px 0 var(--white),2px -2px 0 var(--white),-2px 2px 0 var(--white),3px 3px 0 var(--teal),-3px -3px 0 var(--teal),3px -3px 0 var(--teal),-3px 3px 0 var(--teal)}
  .title--brain{top:216px;color:var(--teal);text-shadow:2px 2px 0 var(--white),-2px -2px 0 var(--white),2px -2px 0 var(--white),-2px 2px 0 var(--white),3px 3px 0 var(--maroon),-3px -3px 0 var(--maroon),3px -3px 0 var(--maroon),-3px 3px 0 var(--maroon)}
  .intro{left:20px;top:290px;width:349px;text-align:center;font-size:12.5px;line-height:16.5px}
  .steps-blob{left:0;top:365px}
  .steps-heading{left:31px;top:396px;width:327px;height:26px;border-radius:13px;background:var(--teal);color:var(--white);font-weight:600;font-size:14.5px;line-height:27px;padding-left:24px;white-space:nowrap}
  .steps-list{left:48px;top:446px;width:296px;list-style:none;color:var(--white);font-size:11.8px;line-height:15.5px}
  .steps-list li{position:relative;padding-left:18px;margin-bottom:7px}
  .steps-list svg{position:absolute;left:0;top:2px}
  .small-changes{left:40px;top:672px;width:210px;text-align:right;color:var(--white);font-weight:700;font-size:12.8px;line-height:18.5px;white-space:nowrap}
  .salad-bowl{left:257px;top:663px;width:96px;height:90px;border-radius:50%;background:radial-gradient(circle at 50% 40%,#9bc06a 0%,#c7473c 45%,#1a1a1a 72%)}
  .talk-doctor{left:40px;top:768px;width:160px;color:var(--teal);font-weight:700;font-size:14px;line-height:18.5px}
  .talk-doctor b{color:var(--maroon)}
  .quote-box{left:197px;top:764px;width:157px;height:60px;border:1px solid var(--maroon);font-size:9.8px;line-height:13px;padding:12px 6px 0 10px}
  .quote-mark{color:#b6a9a9;font-size:22px;background:var(--paper);padding:0 3px;line-height:1}
  .quote-author{left:250px;top:817px;width:82px;text-align:center;font-size:9.8px;line-height:13px;background:var(--paper)}
  .food-strip{left:0;top:846px;width:389px;height:54px;background:linear-gradient(90deg,#5c8b3c,#d7a246,#c9472f,#8a5b3a,#e08a55,#5e7d3a)}

  /* back */
  .recipe-title{left:0;top:36px;width:389px;text-align:center;font-size:37px;line-height:1;color:var(--maroon);white-space:nowrap}
  .rule{height:1.5px;background:var(--maroon)}
  .recipe-name{left:0;top:84px;width:389px;text-align:center;color:var(--teal);font-weight:700;font-size:17px;line-height:24px;white-space:nowrap}
  .plate-photo{left:37px;top:126px;width:131px;height:131px;border-radius:50%;background:radial-gradient(circle at 50% 50%,#d9773f 0%,#5f8a3a 45%,#f0ede6 70%,#e6e2dc 100%)}
  .ingredients-tag{left:188px;top:130px;width:142px;height:27px;border-radius:14px;background:var(--teal);border:2px solid var(--paper);outline:1.5px solid var(--maroon);color:var(--white);font-weight:600;font-size:15px;line-height:24px;text-align:center}
  .ingredients-list{left:188px;top:170px;list-style:none;color:var(--maroon);font-weight:700;font-size:10.8px;line-height:14.4px;white-space:nowrap}
  .method{left:34px;top:268px;width:330px;font-size:10.8px;line-height:15px}
  .heritage-quote{left:16px;top:388px}
  .heritage-text{left:49px;top:420px;width:290px;text-align:center;color:var(--white);font-weight:600;font-size:13.2px;line-height:18px}
  .info-heading{left:0;top:546px;width:389px;text-align:center;color:var(--maroon);font-weight:700;font-size:14px}
  .info-heading span{background:var(--paper);padding:0 14px;position:relative}
  .info-line{left:44px;top:556px;width:302px;height:1px;background:var(--teal)}
  .topic{left:0;width:389px;text-align:center;font-weight:700;font-size:14px;line-height:18px}
  .source{left:0;width:389px;text-align:center;color:var(--teal);font-weight:700;font-size:11.5px;line-height:14px}
  .source-plain{left:0;width:389px;text-align:center;font-size:11px;line-height:14.5px}
  .url-pill{left:61px;width:266px;height:22px;border:1.2px solid var(--teal);border-radius:11px;text-align:center;font-size:12px;line-height:20px;color:var(--maroon);white-space:nowrap}
  .org-mark{left:96px;top:782px;display:flex;align-items:center;gap:10px}
  .org-dot{width:48px;height:48px;border-radius:50%;background:var(--teal)}
  .org-name{color:var(--teal);font-weight:600;font-size:17px}
  .funding{left:27px;top:843px;width:335px;font-family:"Arimo",Arial,sans-serif;font-size:6.4px;line-height:8px;text-align:justify;color:#222}
</style>
</head>
<body>

<section class="card card--front">
  <div class="abs food-collage" role="img" aria-label="Collage of healthy foods: avocado, salmon, berries, beans, eggs, vegetables and lean meat"></div>
  <h1 class="abs title title--food display">Healthy Food</h1>
  <h2 class="abs title title--brain display">Healthy Brain</h2>
  <p class="abs intro">Everyone slows down as they get older, both in body and mind. Eating healthier food can help your overall health, including brain health. It may also reduce your risk for memory loss and problems thinking.</p>

  <svg class="abs steps-blob" width="389" height="395" viewBox="0 0 389 395">
    <path fill="var(--maroon)" d="M70 18 C120 -2 250 0 300 8 C345 14 372 30 372 80 L372 300 C372 360 350 390 300 392 C230 395 120 392 80 390 C55 388 50 370 60 350 C55 330 35 320 30 290 L28 80 C28 40 40 26 70 18 Z"/>
    <path fill="var(--maroon)" d="M336 10 C350 0 370 12 372 32 C366 36 350 24 336 10 Z"/>
    <path fill="var(--maroon)" d="M18 320 C30 305 52 318 60 345 C52 352 25 342 18 320 Z"/>
  </svg>
  <div class="abs steps-heading">Healthier steps to protect your brain:</div>
  <ul class="abs steps-list">
    <li><svg width="11" height="11" viewBox="0 0 12 12"><circle cx="6" cy="6" r="5.2" fill="none" stroke="#fff" stroke-width="1"/><path d="M3.5 6.2 L5.3 7.9 L8.6 4.3" fill="none" stroke="#fff" stroke-width="1.1"/></svg>Eat more vegetables, fruits, whole grains, and lower-fat milk</li>
    <li><svg width="11" height="11" viewBox="0 0 12 12"><circle cx="6" cy="6" r="5.2" fill="none" stroke="#fff" stroke-width="1"/><path d="M3.5 6.2 L5.3 7.9 L8.6 4.3" fill="none" stroke="#fff" stroke-width="1.1"/></svg>Use less salt and added sugar</li>
    <li><svg width="11" height="11" viewBox="0 0 12 12"><circle cx="6" cy="6" r="5.2" fill="none" stroke="#fff" stroke-width="1"/><path d="M3.5 6.2 L5.3 7.9 L8.6 4.3" fill="none" stroke="#fff" stroke-width="1.1"/></svg>Eat more fish, chicken, turkey, beans, and nuts</li>
    <li><svg width="11" height="11" viewBox="0 0 12 12"><circle cx="6" cy="6" r="5.2" fill="none" stroke="#fff" stroke-width="1"/><path d="M3.5 6.2 L5.3 7.9 L8.6 4.3" fill="none" stroke="#fff" stroke-width="1.1"/></svg>Cut down on bad fats ("saturated" and trans), cholesterol, and red meat</li>
    <li><svg width="11" height="11" viewBox="0 0 12 12"><circle cx="6" cy="6" r="5.2" fill="none" stroke="#fff" stroke-width="1"/><path d="M3.5 6.2 L5.3 7.9 L8.6 4.3" fill="none" stroke="#fff" stroke-width="1.1"/></svg>Buy fresh, not packaged food when you can</li>
    <li><svg width="11" height="11" viewBox="0 0 12 12"><circle cx="6" cy="6" r="5.2" fill="none" stroke="#fff" stroke-width="1"/><path d="M3.5 6.2 L5.3 7.9 L8.6 4.3" fill="none" stroke="#fff" stroke-width="1.1"/></svg>Limit how much alcohol you drink</li>
    <li><svg width="11" height="11" viewBox="0 0 12 12"><circle cx="6" cy="6" r="5.2" fill="none" stroke="#fff" stroke-width="1"/><path d="M3.5 6.2 L5.3 7.9 L8.6 4.3" fill="none" stroke="#fff" stroke-width="1.1"/></svg>Learn your daily calorie needs for your body size</li>
    <li><svg width="11" height="11" viewBox="0 0 12 12"><circle cx="6" cy="6" r="5.2" fill="none" stroke="#fff" stroke-width="1"/><path d="M3.5 6.2 L5.3 7.9 L8.6 4.3" fill="none" stroke="#fff" stroke-width="1.1"/></svg>Take care of your mental and spiritual health to support your physical and brain health</li>
  </ul>
  <p class="abs small-changes">Small changes can<br>make a big difference for<br>better brain health.</p>
  <div class="abs salad-bowl" role="img" aria-label="Bowl of fresh green salad with tomatoes"></div>

  <p class="abs talk-doctor">Talk to your <b>Doctor</b> about more steps to healthier food choices.</p>
  <div class="abs quote-box">Without the elk, salmon, huckleberries, shellfish, and cedar trees we are nobody...</div>
  <span class="abs quote-mark display" style="left:206px;top:754px">“</span>
  <p class="abs quote-author">Lena Marwick<br>(Cedar River)</p>
  <span class="abs quote-mark display" style="left:334px;top:818px">”</span>
  <div class="abs food-strip" role="img" aria-label="Row of fresh produce: greens, avocado, lime, tomatoes, beans and salmon"></div>
</section>

<section class="card card--back">
  <h2 class="abs recipe-title display">Make This at Home</h2>
  <div class="abs rule" style="left:39px;top:80px;width:311px"></div>
  <h3 class="abs recipe-name">Grilled Salmon &amp; Veggie Foil Packets</h3>
  <div class="abs rule" style="left:39px;top:112px;width:311px"></div>

  <div class="abs plate-photo" role="img" aria-label="Plate of grilled salmon with asparagus, roasted tomato, garlic and lemon"></div>
  <div class="abs ingredients-tag">Ingredients:</div>
  <ul class="abs ingredients-list">
    <li>Salmon , Asparagus</li>
    <li>Red or Green Peppers</li>
    <li>(Or any seasonal vegetable)</li>
    <li>Onion , Lemon – sliced</li>
    <li>Basil , Olive Oil</li>
    <li>Salt and Pepper , Garlic Powder</li>
  </ul>

  <p class="abs method">Cut asparagus, peppers, and onion into bite-size pieces. Cut salmon into 4-6 oz pieces. Tear tin foil large enough to wrap around salmon &amp; veggies (2 layers). Add veggies and salmon to foil. Drizzle with olive oil, season with salt, pepper, basil, garlic &amp; top with a piece of sliced lemon. Wrap foil tightly around food. Grill at 400 degrees for about 20 minutes. Careful opening!</p>

  <svg class="abs heritage-quote" width="360" height="148" viewBox="0 0 360 148">
    <path fill="var(--maroon)" d="M10 6 L340 2 L334 20 L350 34 L338 52 L356 70 L340 90 L358 110 L344 130 L352 146 L36 144 L48 128 L26 112 L40 96 L4 80 L30 64 L12 46 L34 30 L6 20 Z"/>
    <text x="36" y="42" font-family="Chewy, 'Comic Sans MS', cursive" font-size="46" fill="#fff">“</text>
    <text x="298" y="152" font-family="Chewy, 'Comic Sans MS', cursive" font-size="46" fill="#fff">”</text>
  </svg>
  <p class="abs heritage-text">Food &amp; drink are a source of<br>strength and connection to community.<br>A return to traditional food pathways and<br>eating local, seasonal fresh<br>foods make healthier eating easier.</p>

  <div class="abs info-line"></div>
  <h4 class="abs info-heading"><span>For More Information</span></h4>

  <p class="abs topic" style="top:572px">ABOUT HEALTHIER EATING</p>
  <p class="abs source" style="top:598px">PlateWise Eating</p>
  <p class="abs url-pill" style="top:614px">https://www.platewise.org</p>

  <p class="abs topic" style="top:644px">ABOUT BRAIN HEALTH</p>
  <p class="abs source-plain" style="top:662px">Velmor Collective Center for<br>Brain Health</p>
  <p class="abs url-pill" style="top:694px">https://velmorcollective.org/mind-care/</p>

  <p class="abs source" style="top:726px">Northfield Healthy Aging Program</p>
  <p class="abs url-pill" style="top:743px">https://www.northfieldaging.org</p>

  <div class="abs org-mark">
    <span class="org-dot"></span>
    <span class="org-name">Velmor Collective</span>
  </div>

  <p class="abs funding">This product is supported by the Northfield Public Health Foundation (NPHF) as part of a financial assistance award totaling $348,711 with 100 percent funded by NPHF. The contents are those of the author(s) and do not necessarily represent the official views of, nor an endorsement, by NPHF or its partners.</p>
</section>

</body>
</html>
```